Copperleaf Vantage Training PowerPoint Template

I want to PowerPoint template theme using my attached logo. My colors are black and orange. My website is CopperleafVantage.com. I am a handgun training company.

Font:

- Serpentine-Bold-Bold for "IRON BRAE"

- BrowalliaUPC for "SHOOTING SPORTS"

Colors (CMYK code):

- BLACK ....... 0; 0; 0; 100;
- ORANGE ... gradient from 0; 65; 97.5; 0 to 0; 39; 97.5; 0

```html
<!DOCTYPE html>
<html lang="en">
<head>
<meta charset="utf-8">
<title>Copperleaf Vantage Training – Slide Template</title>
<link rel="stylesheet" href="https://fonts.googleapis.com/css2?family=Anton&display=swap">
<style>
  :root {
    --bg-dark: #1b2326;
    --bg-dark-edge: #141a1c;
    --rule-grey: #7b8487;
    --orange-deep: #e9832a;
    --orange-bright: #f2b21f;
    --panel-white: #ffffff;
    --panel-glow: rgba(240, 180, 30, 0.85);
    --brand-ink: #131719;
  }
  * { margin: 0; padding: 0; box-sizing: border-box; }
  html, body {
    width: 1200px;
    height: 900px;
    overflow: hidden;
  }
  body {
    position: relative;
    background: radial-gradient(ellipse at 50% 40%, var(--bg-dark) 0%, var(--bg-dark-edge) 100%);
    font-family: "Anton", sans-serif;
  }
  .header-rule {
    position: absolute;
    left: 0;
    top: 54px;
    width: 1200px;
    height: 3px;
    background: var(--rule-grey);
  }
  .header-band {
    position: absolute;
    left: 0;
    top: 57px;
    width: 1200px;
    height: 47px;
    background: linear-gradient(90deg, var(--orange-deep) 0%, var(--orange-bright) 50%, var(--orange-deep) 100%);
    box-shadow: 0 2px 4px rgba(0, 0, 0, 0.5);
  }
  .brand {
    position: absolute;
    left: 40px;
    top: 22px;
    display: flex;
    align-items: center;
    gap: 14px;
  }
  .brand-mark {
    width: 120px;
    height: 120px;
    border-radius: 50%;
    background: var(--brand-ink);
  }
  .brand-name {
    color: var(--brand-ink);
    font-size: 22px;
    line-height: 1.05;
    letter-spacing: 1px;
    text-transform: uppercase;
  }
  .content-panel {
    position: absolute;
    left: 39px;
    top: 175px;
    width: 1119px;
    height: 690px;
    background: var(--panel-white);
    border-radius: 12px;
    border: 2px solid #e8e8e8;
    box-shadow: 0 0 14px 4px var(--panel-glow), 6px 8px 18px rgba(240, 180, 30, 0.6);
  }
</style>
</head>
<body>
  <div class="header-rule"></div>
  <div class="header-band"></div>
  <div class="brand">
    <div class="brand-mark"></div>
    <div class="brand-name">Copperleaf Vantage<br>Training</div>
  </div>
  <main class="content-panel"></main>
</body>
</html>
```